Interactive Report Dashboard for Data Analytics

Please see this google doc for information and pictures regarding our project.
https://files.plomvex.com/doc/8TrwQ2mZpLx4VnKc0sYd7HjE3fRb9uNa5Gq/view?share=open
Feel free to message me if you have any questions.
Target Market(s)
This is for video producers, youtubers, and online teachers.
We run focus groups for them and help them understand how their audience reacts to the video content.
Coding
Coded - Design and coding required
Number of Pages Required
5+ page
Colors
Designer to choose colors to be used in the design.
Look and feel
Each slider illustrates characteristics of the customer's brand and the style your logo design should communicate.

```html
<!DOCTYPE html>
<html lang="en">
<head>
<meta charset="utf-8">
<title>Vantora – My Summary Reports</title>
<link href="https://fonts.googleapis.com/css2?family=Montserrat:wght@400;500;600;700&display=swap" rel="stylesheet">
<style>
:root{
  --bg:#efefef;
  --sidebar:#f0f0f0;
  --line:#dcdcdc;
  --white:#ffffff;
  --ink:#222222;
  --muted:#8a8a8a;
  --accent:#2d9bf0;
  --active-bg:#dde8f3;
  --campaign:#cfcfcf;
  --row-tint:#eaf3fc;
  --row-plain:#f6f6f6;
  --head-tint:#e3edf8;
  --filter:#555555;
  --footer:#000000;
  --footer-text:#b5b5b5;
  --footer-dim:#6f6f6f;
  --bar-blue:#4285f4;
}
*{box-sizing:border-box;margin:0;padding:0}
html,body{width:1200px;height:1112px;overflow:hidden}
body{font-family:'Montserrat',sans-serif;background:var(--bg);color:var(--ink);position:relative}
.abs{position:absolute}

/* Sidebar */
.sidebar{left:0;top:0;width:180px;height:798px;background:var(--sidebar);border-right:1px solid var(--line)}
.brand{left:0;top:0;width:180px;height:54px;border-bottom:1px solid var(--line);display:flex;align-items:center;justify-content:center;gap:6px}
.brand-mark{width:12px;height:12px;border-radius:50%;background:var(--accent)}
.brand-name{font-size:14px;font-weight:600;color:var(--accent)}
.avatar{left:68px;top:66px;width:44px;height:44px;border-radius:50%;background:radial-gradient(circle at 55% 40%,#8a3a2a,#1b1d2a 70%)}
.user-name{left:0;top:117px;width:180px;text-align:center;font-size:9.5px;color:var(--muted)}
.section-label{left:13px;top:159px;font-size:9px;font-weight:500;color:var(--ink)}
.nav-item{left:0;width:180px;height:30px;display:flex;align-items:center;font-size:9.5px;color:var(--muted)}
.nav-item .icon{width:32px;display:flex;justify-content:center}
.nav-item.active{background:var(--active-bg);color:var(--accent);border-right:2px solid var(--accent);height:37px}
.new-campaign{left:0;top:422px;width:180px;height:32px;background:var(--campaign);color:var(--white);font-size:11px;font-weight:600;display:flex;align-items:center;padding-left:16px}
.toggle{left:8px;top:537px;width:34px;height:17px;border-radius:9px;background:var(--white);box-shadow:0 0 2px rgba(0,0,0,.15)}
.toggle span{position:absolute;left:1px;top:1px;width:15px;height:15px;border-radius:50%;background:var(--accent)}

/* Top bar */
.topbar{left:180px;top:0;width:1020px;height:54px;border-bottom:1px solid var(--line);background:var(--bg)}
.page-title{left:207px;top:18px;font-size:14.5px;font-weight:500}
.search{left:696px;top:11px;width:409px;height:31px;background:#d9d9d9;border-radius:3px 0 0 3px;font-size:8px;color:var(--muted);display:flex;align-items:center;gap:6px;padding-left:10px}
.search-btn{left:1105px;top:11px;width:49px;height:31px;background:var(--accent);color:var(--white);font-size:9px;font-weight:600;display:flex;align-items:center;justify-content:center;border-radius:0 3px 3px 0}
.bell{left:1163px;top:19px}

/* Hero */
.hero{left:186px;top:60px;width:1014px;height:278px;background:var(--white)}
.hero-title{left:218px;top:189px;font-size:15.5px;font-weight:600}
.filter-bar{left:696px;top:91px;width:478px;height:38px;background:var(--filter);border:1px solid #444}
.tabs{left:186px;top:310px;width:1014px;height:28px;border-bottom:1px solid var(--line)}
.tab{top:316px;font-size:9px;font-weight:500;color:#666}
.tab.current{color:var(--ink);font-weight:600}
.tab-underline{left:492px;top:335px;width:118px;height:2px;background:var(--accent)}

/* Survey left column */
.card{height:31px;background:var(--white);box-shadow:0 4px 6px rgba(0,0,0,.15);display:flex;align-items:center;justify-content:center;font-size:8.5px;font-weight:600}
.group-label{font-size:8.5px;font-weight:500;color:#7d7d7d;text-align:center}

/* Table */
.table{left:631px;top:345px;width:559px;border-collapse:collapse;font-size:8.8px;table-layout:fixed}
.table th{background:var(--head-tint);font-weight:600;height:19px;border-right:1px solid #c8d7e8}
.table td{vertical-align:top;text-align:center;padding-top:6px;line-height:1.45;border-right:1px solid #c8d7e8;border-bottom:1px solid #d6dde6}
.table .tint td{background:var(--row-tint);height:48px}
.table .plain td{background:var(--row-plain);height:51px}
.table th:last-child,.table td:last-child{border-right:none}
.table td.panel{background:var(--white);height:189px;padding:0;border-right:none}
.stat{font-size:7.5px;color:#777}
.stat-val{font-size:8px;font-weight:600;color:#888}

/* Footer */
.footer{left:0;top:798px;width:1200px;height:314px;background:var(--footer);color:var(--footer-text)}
.f-brand{left:254px;top:864px;font-size:12px;font-weight:600;color:var(--accent);display:flex;align-items:center;gap:6px}
.f-head{top:850px;font-size:8px;font-weight:500;color:var(--footer-text)}
.f-link{font-size:7.5px;color:var(--footer-text)}
.f-social{top:855px;width:18px;height:18px;border-radius:50%;background:#9a9a9a}
.f-rule{left:241px;top:1001px;width:719px;height:1px;background:#2a2a2a}
.f-small{top:1038px;font-size:7.5px;color:var(--footer-dim)}
.made{left:566px;top:1027px;font-size:9px;font-weight:600;color:var(--white);display:flex;align-items:center;gap:6px}
.copy{left:726px;top:1031px;font-size:7.5px;color:var(--footer-text)}
</style>
</head>
<body>

<!-- Sidebar -->
<aside class="abs sidebar"></aside>
<div class="abs brand"><span class="brand-mark"></span><span class="brand-name">Vantora</span></div>
<div class="abs avatar" role="img" aria-label="User profile photo"></div>
<div class="abs user-name">Evan Marlow &#8964;</div>
<div class="abs section-label">ACCOUNT</div>

<div class="abs nav-item" style="top:185px"><span class="icon"><svg width="10" height="10" viewBox="0 0 10 10"><path d="M1 5L5 1l4 4v4H6V6H4v3H1z" fill="#777"/></svg></span>Dashboard</div>
<div class="abs nav-item" style="top:223px"><span class="icon"><svg width="10" height="8" viewBox="0 0 10 8"><rect x="0.5" y="0.5" width="9" height="6" fill="none" stroke="#888"/></svg></span>Messages<svg style="margin-left:auto;margin-right:14px" width="8" height="5" viewBox="0 0 8 5"><path d="M1 1l3 3 3-3" fill="none" stroke="#888"/></svg></div>
<div class="abs nav-item active" style="top:258px"><span class="icon"><svg width="14" height="8" viewBox="0 0 14 8"><path d="M0 4h3l2-3 3 6 2-3h4" fill="none" stroke="#2d9bf0" stroke-width="1.2"/></svg></span>My Summary Reports</div>
<div class="abs nav-item" style="top:299px"><span class="icon"><svg width="8" height="9" viewBox="0 0 8 9"><circle cx="4" cy="2.5" r="2" fill="none" stroke="#888"/><path d="M0.5 9c0-3 7-3 7 0" fill="none" stroke="#888"/></svg></span>Public profile</div>
<div class="abs nav-item" style="top:337px"><span class="icon"><svg width="10" height="8" viewBox="0 0 10 8"><rect x="0.5" y="0.5" width="9" height="7" fill="none" stroke="#888"/><path d="M3.5 1v6M6.5 1v6" stroke="#888"/></svg></span>Plans</div>
<div class="abs nav-item" style="top:375px"><span class="icon"><svg width="10" height="10" viewBox="0 0 10 10"><path d="M5 0.5l1.4 3 3.1.3-2.4 2 .8 3.2L5 7.3 2.1 9l.8-3.2-2.4-2 3.1-.3z" fill="#777"/></svg></span>Affiliate Marketing</div>
<div class="abs new-campaign">+ NEW CAMPAIGN</div>
<div class="abs nav-item" style="top:458px;font-size:10.5px"><span class="icon"><svg width="9" height="9" viewBox="0 0 9 9"><circle cx="4.5" cy="4.5" r="3" fill="none" stroke="#777" stroke-width="2" stroke-dasharray="2 1"/></svg></span>Settings</div>
<div class="abs nav-item" style="top:495px"><span class="icon"><svg width="9" height="9" viewBox="0 0 9 9"><path d="M6 1.5A3.5 3.5 0 1 0 6 7.5M4 4.5h5" fill="none" stroke="#888"/></svg></span>Sign out</div>
<div class="abs toggle"><span></span></div>

<!-- Top bar -->
<header class="abs topbar"></header>
<h1 class="abs page-title">My Summary Reports</h1>
<div class="abs search"><svg width="9" height="9" viewBox="0 0 9 9"><circle cx="3.5" cy="3.5" r="2.8" fill="none" stroke="#999"/><path d="M5.7 5.7L8.5 8.5" stroke="#999"/></svg>Search...</div>
<div class="abs search-btn">Search</div>
<svg class="abs bell" width="13" height="14" viewBox="0 0 13 14"><path d="M6.5 1a4 4 0 0 0-4 4v3.5L1 10.5h11L10.5 8.5V5a4 4 0 0 0-4-4z" fill="#666"/><circle cx="6.5" cy="12" r="1.6" fill="#666"/></svg>

<!-- Hero -->
<section class="abs hero"></section>
<h2 class="abs hero-title">All in One Screener for Every Graph</h2>
<div class="abs filter-bar"></div>
<svg class="abs" style="left:696px;top:91px" width="478" height="38" viewBox="0 0 478 38">
  <g font-family="Montserrat,sans-serif" font-size="3.5" fill="#ddd">
    <text x="12" y="9">Age</text><text x="5" y="16">Income</text>
  </g>
  <rect x="32" y="6" width="60" height="3" rx="1.5" fill="#ccc"/><rect x="36" y="6" width="52" height="3" rx="1.5" fill="#4a8fe0"/>
  <rect x="32" y="13" width="60" height="3" rx="1.5" fill="#ccc"/><rect x="34" y="13" width="58" height="3" rx="1.5" fill="#4a8fe0"/>
  <g fill="#eee"><rect x="10" y="26" width="55" height="5"/><rect x="70" y="26" width="55" height="5"/><rect x="130" y="26" width="55" height="5"/><rect x="190" y="26" width="55" height="5"/><rect x="250" y="26" width="55" height="5"/></g>
  <g font-family="Montserrat,sans-serif" font-size="3" fill="#888"><text x="12" y="29.8">Gender</text><text x="72" y="29.8">Region</text><text x="132" y="29.8">Device</text><text x="192" y="29.8">Source</text><text x="252" y="29.8">Language</text></g>
</svg>
<svg class="abs" style="left:696px;top:160px" width="478" height="125" viewBox="0 0 478 125">
  <g stroke="#ececec"><line x1="0" y1="7" x2="478" y2="7"/><line x1="0" y1="47" x2="478" y2="47"/><line x1="0" y1="87" x2="478" y2="87"/></g>
  <rect x="15" y="64" width="50" height="56" fill="#4fb3d9"/>
  <rect x="95" y="32" width="50" height="88" fill="#b94fe6"/>
  <rect x="175" y="32" width="50" height="88" fill="#00e640"/>
  <rect x="255" y="72" width="50" height="48" fill="#d95a00"/>
  <rect x="336" y="26" width="50" height="94" fill="#e0201e"/>
  <rect x="416" y="6" width="50" height="114" fill="#f7bb3a"/>
  <g font-family="Montserrat,sans-serif" font-size="4.5" fill="#fff" text-anchor="middle">
    <text x="40" y="69">Disgust</text><text x="120" y="37">Fear</text><text x="200" y="37">Happiness</text><text x="280" y="77">Sadness</text><text x="361" y="31">Anger</text><text x="441" y="11">Surprise</text>
  </g>
</svg>

<nav class="abs tabs"></nav>
<div class="abs tab" style="left:206px">Audience Analytic Tools</div>
<div class="abs tab" style="left:351px">Real Time Emotion Display</div>
<div class="abs tab current" style="left:511px">Survey Responses</div>
<div class="abs tab-underline"></div>

<!-- Survey groups -->
<div class="abs card" style="left:211px;top:358px;width:215px">Personality Test Question Responses</div>
<div class="abs card" style="left:460px;top:358px;width:156px">Question 1</div>
<div class="abs group-label" style="left:211px;top:465px;width:215px">Demography Question Responses</div>
<div class="abs group-label" style="left:460px;top:465px;width:156px">Question 2</div>
<div class="abs group-label" style="left:211px;top:563px;width:215px">Political Question Responses</div>
<div class="abs group-label" style="left:460px;top:563px;width:156px">Question 3</div>
<div class="abs group-label" style="left:211px;top:661px;width:215px">Client's Custom Question Responses</div>
<div class="abs group-label" style="left:460px;top:661px;width:156px">Question 4</div>

<!-- Responses table -->
<table class="abs table">
  <colgroup><col style="width:133px"><col style="width:142px"><col style="width:142px"><col style="width:142px"></colgroup>
  <thead><tr><th>Document</th><th>Responses</th><th>Codes</th><th>Comment</th></tr></thead>
  <tbody>
    <tr class="tint"><td>RESP001</td><td>Lorem ipsum dolor sit amet, consectetur adipiscing elit.</td><td></td><td>Lorem ipsum dolor sit amet, consectetur adipiscing elit.</td></tr>
    <tr class="plain"><td>RESP002</td><td>Lorem ipsum dolor sit amet, consectetur adipiscing elit.</td><td></td><td>Lorem ipsum dolor sit amet, consectetur adipiscing elit.</td></tr>
    <tr class="tint"><td>RESP003</td><td>Lorem ipsum dolor sit amet, consectetur adipiscing elit.</td><td></td><td>Lorem ipsum dolor sit amet, consectetur adipiscing elit.</td></tr>
    <tr><td class="panel" colspan="4"></td></tr>
    <tr class="plain"><td>RESP004</td><td>Lorem ipsum dolor sit amet, consectetur adipiscing elit.</td><td></td><td>Lorem ipsum dolor sit amet, consectetur adipiscing elit.</td></tr>
  </tbody>
</table>

<!-- Question 1 panel content -->
<div class="abs" style="left:644px;top:522px;font-size:8.5px;font-weight:700">QUESTION 1</div>
<svg class="abs" style="left:644px;top:538px" width="260" height="152" viewBox="0 0 260 152">
  <g font-family="Montserrat,sans-serif">
    <text x="6" y="6" font-size="4.2" fill="#666">Video reaction scores</text>
    <text x="6" y="12" font-size="3.4" fill="#aaa">share by viewer group</text>
    <text x="154" y="30" font-size="3.4" fill="#555">Percentage</text>
    <g font-size="3.4" fill="#777" text-anchor="middle"><text x="59" y="42">0</text><text x="101" y="42">10</text><text x="143" y="42">20</text><text x="185" y="42">30</text><text x="227" y="42">40</text></g>
    <text transform="translate(11 104) rotate(-90)" font-size="3.4" fill="#777" text-anchor="middle">Segment</text>
    <g font-size="3.2" fill="#777" text-anchor="end"><text x="56" y="52">Opening scene</text><text x="56" y="74">Main topic</text><text x="56" y="96">Key example</text><text x="56" y="118">Closing recap</text><text x="56" y="139">Other</text></g>
  </g>
  <g stroke="#eee"><line x1="59" y1="44" x2="59" y2="148"/><line x1="101" y1="44" x2="101" y2="148"/><line x1="143" y1="44" x2="143" y2="148"/><line x1="185" y1="44" x2="185" y2="148"/><line x1="227" y1="44" x2="227" y2="148"/></g>
  <g fill="var(--bar-blue)">
    <rect x="59" y="43" width="183" height="13"/><rect x="59" y="65" width="128" height="13"/><rect x="59" y="87" width="50" height="13"/><rect x="59" y="109" width="42" height="13"/><rect x="59" y="130" width="12" height="13"/>
  </g>
</svg>
<div class="abs stat" style="left:935px;top:542px">Computer Science</div><div class="abs stat-val" style="left:1059px;top:542px">72&nbsp;&nbsp; 62%</div>
<div class="abs stat" style="left:935px;top:574px">Electronics</div><div class="abs stat-val" style="left:1059px;top:574px">23&nbsp;&nbsp; 20%</div>
<div class="abs stat" style="left:935px;top:606px">Web UX/UI</div><div class="abs stat-val" style="left:1059px;top:606px">4&nbsp;&nbsp; 3%</div>
<div class="abs stat" style="left:935px;top:637px">Data Science</div><div class="abs stat-val" style="left:1059px;top:637px">10</div>

<!-- Footer -->
<footer class="abs footer"></footer>
<div class="abs f-brand"><span class="brand-mark"></span>Vantora</div>
<div class="abs f-head" style="left:408px">ABOUT</div>
<div class="abs f-head" style="left:552px">SUPPORT</div>
<div class="abs f-head" style="left:701px">CONTACT</div>
<div class="abs f-link" style="left:408px;top:895px">About Vantora</div>
<div class="abs f-link" style="left:408px;top:914px">Pricing</div>
<div class="abs f-link" style="left:408px;top:933px">Company</div>
<div class="abs f-link" style="left:408px;top:952px">Jobs</div>
<div class="abs f-link" style="left:408px;top:971px">Blog</div>
<div class="abs f-link" style="left:552px;top:895px">FAQ</div>
<div class="abs f-link" style="left:552px;top:914px">Help Center</div>
<div class="abs f-link" style="left:552px;top:933px">Terms of Service</div>
<div class="abs f-link" style="left:552px;top:952px">Privacy Policy</div>
<div class="abs f-link" style="left:701px;top:895px">Email Us</div>
<div class="abs f-link" style="left:701px;top:914px">Live Chat</div>
<div class="abs f-social" style="left:840px"></div>
<div class="abs f-social" style="left:885px"></div>
<div class="abs f-social" style="left:928px"></div>
<div class="abs f-rule"></div>
<div class="abs f-small" style="left:258px">Privacy Policy</div>
<div class="abs f-small" style="left:335px">Terms Of Use</div>
<div class="abs f-small" style="left:410px">Return Policy</div>
<div class="abs made">Made With <svg width="12" height="11" viewBox="0 0 12 11"><path d="M6 10.5L1.2 5.8A2.9 2.9 0 0 1 6 1.9a2.9 2.9 0 0 1 4.8 3.9z" fill="#e8452c"/></svg></div>
<div class="abs copy">© Vantora. All Rights Reserved.</div>

</body>
</html>
```